Speisekarten
Zielgruppe
we run a restaurant and our target groups are families and business people
Aufgabenstellung
The menu consists of a black folder with 8 DIN A4 slots which have a 2 cm border on all sides. The card should be discreet, classy and easy to read without any kind of complicated fonts or pictures. we would like to see creative designs regarding our recommendation at the end of page 3.

```html
<!DOCTYPE html>
<html lang="de">
<head>
<meta charset="utf-8">
<title>NANEH – Speisekarte</title>
<link href="https://fonts.googleapis.com/css2?family=PT+Sans:wght@400;700&display=swap" rel="stylesheet">
<style>
:root{--bg:#e1e2e4;--paper:#fff;--ink:#2a2a2a;--muted:#707070;--rule:#b8b8b8;--brand:#7a7a7a}
*{box-sizing:border-box;margin:0;padding:0}
html,body{width:1200px;height:3177px;overflow:hidden;background:var(--bg)}
h2,h3{font-weight:400}
.page{position:absolute;width:528px;height:751px;background:var(--paper);box-shadow:3px 4px 7px rgba(0,0,0,.28);padding:0 50px;font-family:'PT Sans',sans-serif;color:var(--ink);font-size:8px;line-height:1.25}
.p1{left:41px;top:41px}.p2{left:632px;top:41px}.p3{left:41px;top:823px}.p4{left:632px;top:823px}
.p5{left:41px;top:1604px}.p6{left:632px;top:1604px}.p7{left:41px;top:2386px}.p8{left:632px;top:2386px}
.brand{text-align:center;color:var(--brand);font-size:15px;letter-spacing:4px;padding-top:58px;height:112px}
.brand .dot{display:block;width:26px;height:26px;border-radius:50%;background:var(--brand);margin:0 auto 6px}
.brand.big{font-size:30px;letter-spacing:2px;padding-top:58px;height:160px}
.brand.big .dot{width:40px;height:40px;margin-bottom:8px}
.title{text-align:center;font-size:12.5px;letter-spacing:.4px;position:relative;padding-bottom:4px;margin-bottom:7px;text-transform:uppercase}
.title::after{content:"";position:absolute;left:50%;bottom:0;width:170px;margin-left:-85px;height:1px;background:linear-gradient(90deg,transparent,var(--rule) 25%,var(--rule) 75%,transparent)}
.title .en{color:var(--muted);margin-left:8px}
.note{text-align:center;font-size:6.3px;margin:-2px 0 8px}
.note .en{color:var(--muted)}
.list{list-style:none}
.row{display:grid;grid-template-columns:1fr 40px 50px;text-transform:uppercase;height:15.4px;align-items:center}
.row span:nth-child(n+2){text-align:right;text-transform:none}
.cols{display:grid;grid-template-columns:1fr 1fr;column-gap:24px}
.dish{margin-bottom:6px}
.dish .h{display:flex;justify-content:space-between;text-transform:uppercase;font-size:8px}
.de{font-size:6.2px;line-height:1.2}
.dish .en{font-size:6.2px;color:var(--muted);line-height:1.2;display:block}
.veg{display:inline-block;width:8px;height:8px;border:.7px solid var(--muted);border-radius:50%;vertical-align:-1px;margin-left:3px;font-size:5px;line-height:7px;text-align:center;color:var(--muted);text-transform:none}
.sec{margin-top:18px}
.foot{position:absolute;left:0;right:0;bottom:50px;text-align:center;font-size:5.6px;line-height:1.45;padding-top:6px}
.foot::before{content:"";position:absolute;top:0;left:50%;width:160px;margin-left:-80px;height:1px;background:linear-gradient(90deg,transparent,var(--rule) 25%,var(--rule) 75%,transparent)}
.foot .en{color:var(--muted)}
.legend{margin-bottom:2px}
.recommend{position:absolute;left:50px;right:50px;bottom:55px;display:flex;align-items:center;justify-content:space-between;text-align:center;font-size:8px;text-transform:uppercase;line-height:1.2}
.recommend .mark{color:var(--brand);font-size:11px;letter-spacing:2px;width:60px}
.recommend .en{color:var(--muted)}
.course{text-align:center;font-size:10.5px}
.course .title{font-size:10.5px;margin:32px auto 8px}
.course .title::after{width:150px;margin-left:-75px}
.course p{line-height:1.25;margin-bottom:9px}
.course .en{color:var(--muted)}
.drinks{display:grid;grid-template-columns:1fr 1fr;column-gap:34px}
.d{display:grid;grid-template-columns:1fr 28px 36px;text-transform:uppercase;height:13.3px;align-items:center;font-size:7.6px}
.d span:nth-child(n+2){text-align:right;text-transform:none}
.d2{display:grid;grid-template-columns:1fr 30px 26px 30px 26px;text-transform:uppercase;height:13.3px;align-items:center;font-size:7.6px}
.d2 span:nth-child(n+2){text-align:right;text-transform:none}
.d.two{grid-template-columns:1fr 36px}
.blk{margin-bottom:18px}
</style>
</head>
<body>

<section class="page p1">
  <div class="brand big"><span class="dot"></span>NANEH</div>
  <h2 class="title">Aperitif</h2>
  <ul class="list">
    <li class="row"><span>Lumen Wild Berry</span><span>0,2 l</span><span>9,00</span></li>
    <li class="row"><span>Hugo</span><span>0,2 l</span><span>8,50</span></li>
    <li class="row"><span>Arancio Spritz</span><span>0,2 l</span><span>8,50</span></li>
    <li class="row"><span>Sekt Arancio</span><span>0,1 l</span><span>8,00</span></li>
    <li class="row"><span>Rossetto Orange</span><span>0,2 l</span><span>7,50</span></li>
    <li class="row"><span>Rossetto Soda</span><span>0,2 l</span><span>7,00</span></li>
    <li class="row"><span>Valdora Bianco / Rosso / Extra Dry</span><span>5 cl</span><span>7,00</span></li>
    <li class="row"><span>Riesling Sekt trocken</span><span>0,1 l</span><span>8,00</span></li>
    <li class="row"><span>Riesling Sekt trocken</span><span>0,75 l</span><span>30,00</span></li>
    <li class="row"><span>Von Reichenau Riesling Brut 2017</span><span>0,75 l</span><span>45,90</span></li>
    <li class="row"><span>Dom Valmont Vintage</span><span>0,75 l</span><span>295,00</span></li>
    <li class="row"><span>Maison Aubrac Brut</span><span>0,2 l</span><span>25,00</span></li>
    <li class="row"><span>Maison Aubrac Brut</span><span>0,75 l</span><span>95,00</span></li>
    <li class="row"><span>Maison Aubrac Rosé</span><span>0,2 l</span><span>28,00</span></li>
    <li class="row"><span>Maison Aubrac Rosé</span><span>0,75 l</span><span>125,00</span></li>
    <li class="row"><span>Clos-Verlaine – Crémant Saphir Brut Vintage Loire</span><span>0,75 l</span><span>45,00</span></li>
    <li class="row"><span>Clos-Verlaine – Crémant Rosé Brut Excellence Loire</span><span>0,75 l</span><span>45,00</span></li>
  </ul>
  <footer class="foot">Haben Sie Fragen zu Zusatzstoffen und Allergenen? Bitte wenden Sie sich an unser Personal!<br><span class="en">Do you have questions about additives and allergens? Please ask our staff!</span><br>Alle Preise in Euro inklusive Mehrwertsteuer. <span class="en">All prices in Euro including VAT.</span></footer>
</section>

<section class="page p2">
  <div class="brand"><span class="dot"></span>NANEH</div>
  <h2 class="title">Vorspeisen<span class="en">Starters</span></h2>
  <div class="cols">
    <div>
      <div class="dish"><div class="h"><span>Kashke-Bademjan<span class="veg">v</span></span><span>11,50</span></div><div class="de">Gebratene und gehackte Auberginen mit einem Hauch Knoblauch, Pfefferminzöl, Röstzwiebeln und Joghurt-Sauce (Kashk)</div><span class="en">Chopped and fried aubergines with a touch of garlic, peppermint, roasted onions and yoghurt sauce (Kashk)</span></div>
      <div class="dish"><div class="h"><span>Mirza Ghassemi<span class="veg">v</span></span><span>11,50</span></div><div class="de">Gegrillte und gehackte Auberginen mit einem Hauch Knoblauch, Tomaten und Ei</div><span class="en">Chopped and grilled aubergines with a touch of garlic, tomatoes and eggs</span></div>
      <div class="dish"><div class="h"><span>Schafskäse</span><span>3,00</span></div><span class="en">Feta cheese</span></div>
      <div class="dish"><div class="h"><span>Hummus<span class="veg">v</span></span><span>6,50</span></div><div class="de">Pürierte Kichererbsen mit einem Hauch Knoblauch und Sesam-Mus</div><span class="en">Pureed chickpeas, sesame nutmeg and a touch of garlic</span></div>
      <div class="dish"><div class="h"><span>Zeytun Parvarde<span class="veg">v</span></span><span>6,50</span></div><div class="de">Grüne Oliven eingelegt in einer Kräuter-Granatapfel-Sauce mit Walnüssen und einem Hauch Knoblauch</div><span class="en">Green olives marinated in an herb-pomegranate-sauce with walnuts and a touch of garlic</span></div>
      <div class="dish"><div class="h"><span>Zeytun<span class="veg">v</span></span><span>4,00</span></div><div class="de">Oliven</div><span class="en">Olives</span></div>
      <div class="dish"><div class="h"><span>Borani Bademjan<span class="veg">v</span></span><span>4,50</span></div><div class="de">Auberginen-Joghurt mit Knoblauch</div><span class="en">Aubergine yoghurt with garlic</span></div>
    </div>
    <div>
      <div class="dish"><div class="h"><span>Borani<span class="veg">v</span></span><span>4,00</span></div><div class="de">Spinat-Joghurt mit einem Hauch Knoblauch</div><span class="en">Spinach yoghurt with a touch of garlic</span></div>
      <div class="dish"><div class="h"><span>Dolmeh<span class="veg">v</span></span><span>5,00</span></div><div class="de">Gefüllte Weinblätter</div><span class="en">Stuffed vine leaves</span></div>
      <div class="dish"><div class="h"><span>Kräuterteller<span class="veg">v</span></span><span>4,00</span></div><div class="de">Basilikum, Minze, Estragon, Petersilie, Schafskäse, Radieschen und Zwiebel</div><span class="en">Basil, peppermint, tarragon, parsley, feta cheese, radishes and onion</span></div>
      <div class="dish"><div class="h"><span>Gemischter Vorspeisenteller</span><span>12,50</span></div><div class="de">ab 2 Personen/pro Person</div><div class="h"><span>Mixed appetizer plate</span></div><span class="en">from 2 persons/per person</span></div>
      <div class="dish"><div class="h"><span>Suppe Djo</span><span>7,00</span></div><div class="de">Perlgraupensuppe</div><span class="en">Barley soup</span></div>
      <div class="dish"><div class="h"><span>Suppe Adas<span class="veg">v</span></span><span>7,00</span></div><div class="de">Linsensuppe</div><span class="en">Lentil soup</span></div>
      <div class="dish"><div class="h"><span>Ashe Reshteh<span class="veg">v</span></span><span>8,00</span></div><div class="de">Nudelsuppe mit Kräutern, Kichererbse, Bohnen, Röstzwiebel und Kashk</div><span class="en">Noodle soup with herbs, chickpeas, beans, roasted onions and kashk</span></div>
    </div>
  </div>
  <h2 class="title sec">Salate<span class="en">Salads</span></h2>
  <div class="cols">
    <div>
      <div class="dish"><div class="h"><span>Gemischter Salat<span class="veg">v</span></span><span>10,90</span></div><div class="de">Salat, Gurken, Tomaten, Oliven, Schafskäse und Mais</div><span class="en">Lettuce, cucumbers, tomatoes, olives, fetacheese and maize</span></div>
      <div class="dish"><div class="h"><span>Salat Shirazi<span class="veg">v</span></span><span>5,00</span></div><div class="de">Fein zerkleinerte Gurken, Tomaten und Zwiebeln, dazu Zitronensaft-Olivenöl-Dressing</div><span class="en">Salad with finely chopped cucumbers, tomatoes, onions with lemon juice and olive oil dressing</span></div>
      <div class="dish"><div class="h"><span>Grüner Salat<span class="veg">v</span></span><span>5,90</span></div><div class="de">Salat, Gurken und Tomaten</div><span class="en">Lettuce with cucumbers and tomatoes</span></div>
    </div>
    <div>
      <div class="dish"><div class="h"><span>Naneh Salat</span><span>19,00</span></div><div class="de">Salat mit gegrillte Maishähnchenbrust, Gurken, Tomaten, Oliven, Schafskäse und Mais</div><span class="en">One skewer of corn chicken breast pieces with salad, olives, cucumber, tomatoes, sheep cheese &amp; corn</span></div>
      <div class="dish"><div class="h"><span>Salat Olvieh</span><span>7,00</span></div><div class="de">Pürierter Kartoffelsalat mit Maishähnchenbrust, Eiern und Salzgurken</div><span class="en">Mashed potato salad with corn chicken breast, eggs and pickled cucumbers</span></div>
      <div class="dish"><div class="h"><span>Dressing</span><span></span></div><div class="de">Honig-Senf Dressing, French Dressing, Essig und Öl</div><span class="en">Honey mustard dressing, French dressing, vinegar and oil</span></div>
    </div>
  </div>
  <footer class="foot"><div class="legend"><span class="veg">v</span> Vegetarische Gerichte <span class="en">Vegetarian Dishes</span> &nbsp;&nbsp; <span class="veg">v</span> Vegane Gerichte <span class="en">Vegan Dishes</span></div>Haben Sie Fragen zu Zusatzstoffen und Allergenen? Bitte wenden Sie sich an unser Personal!<br><span class="en">Do you have questions about additives and allergens? Please ask our staff!</span><br>Alle Preise in Euro inklusive Mehrwertsteuer. <span class="en">All prices in Euro including VAT.</span></footer>
</section>

<section class="page p3">
  <h2 class="title" style="margin-top:52px">Grillgerichte<span class="en">Grill Dishes</span></h2>
  <p class="note">Alle Grillgerichte werden mit Safran verfeinertem Basmatireis und Grilltomate serviert.<br><span class="en">All grilled dishes are served with saffron-refined basmati rice and grilled tomato.</span><br>Alle Gerichte können auf Wunsch gegen 1,00 Euro Aufpreis mit Baghali- oder Sereshk-Polo serviert werden.<br><span class="en">If desired, all dishes can be served with Baghali or Sereshk polo for an additional charge of 1.00 Euro.</span></p>
  <div class="cols">
    <div>
      <div class="dish"><div class="h"><span>Soltani</span><span>28,00</span></div><div class="de">Ein Spieß aus flach geklopftem Lammrücken und ein Lammhackfleisch-Spieß</div><span class="en">One skewer of lamb rack and one of lamb minced meat</span></div>
      <div class="dish"><div class="h"><span>Kubideh</span><span>18,00</span></div><div class="de">Zwei Lammhackfleisch-Spieße</div><span class="en">Two skewers of lamb minced meat</span></div>
      <div class="dish"><div class="h"><span>Djudje</span><span>18,00</span></div><div class="de">Ein Spieß aus Maishähnchenbrust-Stücken</div><span class="en">One skewer of corn chicken breast pieces</span></div>
      <div class="dish"><div class="h"><span>Shishlik</span><span>29,00</span></div><div class="de">Gegrillte Lammkarree-Stücke</div><span class="en">Grilled lamb chops</span></div>
    </div>
    <div>
      <div class="dish"><div class="h"><span>Barg</span><span>23,00</span></div><div class="de">Ein Spieß aus flach geklopftem Lammrücken</div><span class="en">One skewer of lamb rack</span></div>
      <div class="dish"><div class="h"><span>Chenje</span><span>23,00</span></div><div class="de">Ein Spieß aus Lammfilet-Stücken</div><span class="en">One skewer of lamb fillet pieces</span></div>
      <div class="dish"><div class="h"><span>Djudje Soltani</span><span>25,00</span></div><div class="de">Ein Spieß aus Maishähnchenbrust-Stücken und ein Lammhackfleisch-Spieß</div><span class="en">One skewer of corn chicken breast pieces and one of lamb minced meat</span></div>
    </div>
  </div>
  <h2 class="title" style="margin-top:8px">Schmorgerichte<span class="en">Braised Dishes</span></h2>
  <p class="note">Alle Schmorgerichte werden mit Safran verfeinertem Basmatireis serviert.<br><span class="en">All braised dishes are served with saffron rice.</span></p>
  <div class="cols">
    <div>
      <div class="dish"><div class="h"><span>Bamieh</span><span>17,00</span></div><div class="de">Gericht mit Fleischstücken aus der Lammkeule und Okraschoten</div><span class="en">Sauce made from pieces of meat from leg of lamb and okras</span></div>
      <div class="dish"><div class="h"><span>Bademjan</span><span>16,00</span></div><div class="de">Gericht mit Fleischstücken aus der Lammkeule und Auberginen</div><span class="en">Sauce made from pieces of meat from leg of lamb and aubergines</span></div>
      <div class="dish"><div class="h"><span>Fesenjan</span><span>21,00</span></div><div class="de">Gericht aus geriebenen Walnüssen und Granatapfel nach Wahl mit Lammhackbällchen, Maishähnchenbrust oder Maishähnchenkeule</div><span class="en">Sauce made from grated walnut and pomegranate sauce with lamb meatballs, corn chicken breast or corn chicken drumstick</span></div>
    </div>
    <div>
      <div class="dish"><div class="h"><span>Gheimeh Bademjan</span><span>17,00</span></div><div class="de">Gericht mit Fleischstücken aus der Lammkeule, Auberginen und Linsen</div><span class="en">Sauce made from pieces of meat from leg of lamb, aubergines and lentil</span></div>
      <div class="dish"><div class="h"><span>Ghorme Sabsi</span><span>16,00</span></div><div class="de">Gericht mit Fleischstücken aus der Lammkeule, Bohnen, Limette und verschiedenen Kräutern (Schnittlauch, Petersilie, Bockshornklee)</div><span class="en">Sauce made from pieces of meat from leg of lamb, beans, lemon and various herbs (chives, parsley, fenugreek)</span></div>
    </div>
  </div>
  <h2 class="title" style="margin-top:8px">Reisgerichte<span class="en">Rice Dishes</span></h2>
  <div class="cols">
    <div>
      <div class="dish"><div class="h"><span>Baghali Polo ba Mahiche</span><span>22,00</span></div><div class="de">Geschmorte Lammhaxe, serviert mit Basmatireis mit dicken Bohnen und Dillspitzen, verfeinert mit Safran und Zimt</div><span class="en">Braised knuckle of lamb, served with basmati rice with beans, dill tips and cinnamon</span></div>
      <div class="dish"><div class="h"><span>Sereshk Polo ba Mahiche</span><span>22,00</span></div><div class="de">Geschmorte Lammhaxe, serviert mit Basmatireis mit gebratenen Berberitzen</div><span class="en">Braised knuckle of lamb, served with basmati rice with fried berberis</span></div>
      <div class="dish"><div class="h"><span>Shirin Polo ba Morgh</span><span>18,00</span></div><div class="de">Geschmorte Maishähnchenkeule, serviert mit Basmatireis mit Mandelsplittern, gehackten Pistazien, Orangenschale und Karotten</div><span class="en">Braised corn chicken drumstick, served with basmati rice with slivered almonds, chopped pistachios, orange peel and carrots</span></div>
    </div>
    <div>
      <div class="dish"><div class="h"><span>Baghali Polo ba Morgh</span><span>18,00</span></div><div class="de">Geschmorte Maishähnchenkeule, serviert mit Basmatireis mit dicken Bohnen und Dillspitzen, verfeinert mit Safran und Zimt</div><span class="en">Braised corn chicken drumstick, served with basmati rice with beans, dill tips and cinnamon</span></div>
      <div class="dish"><div class="h"><span>Sereshk Polo ba Morgh</span><span>18,00</span></div><div class="de">Geschmorte Maishähnchenkeule, serviert mit Basmatireis mit gebratenen Berberitzen</div><span class="en">Braised corn chicken drumstick, served with basmati rice with fried berberis</span></div>
    </div>
  </div>
  <div class="recommend">
    <span class="mark">NANEH</span>
    <p>Wir empfehlen Ihnen zu unseren Hauptgerichten Masto Musir,<br>Masto Khiar, Salat Shirazi oder unsere hausgemachte Chili Sauce.<br><span class="en">We recommend Masto Musir, Masto Khiar, Salad Shirazi<br>or our homemade chili sauce for our main dishes.</span></p>
    <span class="mark">NANEH</span>
  </div>
</section>

<section class="page p4">
  <h2 class="title" style="margin-top:52px">Vegetarisch / Vegan<span class="en">Vegetarian / Vegan</span></h2>
  <div class="cols">
    <div>
      <div class="dish"><div class="h"><span>Bademjan vegetarisch<span class="veg">v</span></span><span>12,00</span></div><div class="de">Auberginen in Tomatensauce</div><span class="en">Aubergines in tomato sauce</span></div>
      <div class="dish"><div class="h"><span>Falafel Hummus Teller<span class="veg">v</span></span><span>16,00</span></div><div class="de">Falafel hummus plate</div></div>
      <div class="dish"><div class="h"><span>Gegrilltes Gemüse<span class="veg">v</span></span><span>11,00</span></div><span class="en">Grilled vegetables</span></div>
    </div>
    <div>
      <div class="dish"><div class="h"><span>Bamieh vegetarisch<span class="veg">v</span></span><span>12,00</span></div><div class="de">Okraschoten in Tomatensauce</div><span class="en">Okras in tomato sauce</span></div>
      <div class="dish"><div class="h"><span>Fesenjan vegetarisch<span class="veg">v</span></span><span>12,00</span></div><div class="de">Gericht aus geriebenen Walnüssen und Granatapfel-Mark</div><span class="en">Sauce made from grated walnut and pomegranate sauce</span></div>
    </div>
  </div>
  <h2 class="title" style="margin-top:12px">Beilagen / Extras<span class="en">Side Dishes / Extras</span></h2>
  <div class="cols">
    <div>
      <div class="dish"><div class="h"><span>Masto Musir<span class="veg">v</span></span><span>4,00</span></div><div class="de">Joghurt mit wildem Knoblauch</div><span class="en">Yoghurt with wild garlic</span></div>
      <div class="dish"><div class="h"><span>Masto Khiar<span class="veg">v</span></span><span>4,00</span></div><div class="de">Joghurt mit Gurken und Minze</div><span class="en">Yoghurt with cucumbers and peppermint</span></div>
      <div class="dish"><div class="h"><span>Khiar Shour<span class="veg">v</span></span><span>3,00</span></div><div class="de">Salzgurken nach persischer Art</div><span class="en">Pickled cucumbers Persian style</span></div>
      <div class="dish"><div class="h"><span>Torshi<span class="veg">v</span></span><span>4,00</span></div><div class="de">Sauer eingelegtes Gemüse</div><span class="en">Sour pickled vegetables</span></div>
      <div class="dish"><div class="h"><span>Shirin Polo<span class="veg">v</span></span><span>6,00</span></div><div class="de">Basmatireis mit Mandelsplittern, gehackten Pistazien, Orangenschale und Karotten</div><span class="en">Basmati rice with slivered almonds, chopped pistachios, orange peel and carrots</span></div>
      <div class="dish"><div class="h"><span>Hausgemachte Chili-Sauce</span><span>1,00</span></div><span class="en">Home-made chili sauce</span></div>
      <div class="dish"><div class="h"><span>Pommes<span class="veg">v</span></span><span>6,00</span></div><span class="en">French fries</span></div>
    </div>
    <div>
      <div class="dish"><div class="h"><span>Basmatireis<span class="veg">v</span></span><span>4,00</span></div><span class="en">Basmati rice</span></div>
      <div class="dish"><div class="h"><span>Baghali Polo<span class="veg">v</span></span><span>5,50</span></div><div class="de">Basmatireis mit dicken Bohnen und Dillspitze, verfeinert mit Safran und Zimt</div><span class="en">Basmati rice with beans, dill tips and cinnamon</span></div>
      <div class="dish"><div class="h"><span>Sereshk Polo<span class="veg">v</span></span><span>5,50</span></div><div class="de">Basmatireis mit gebratenen Berberitzen</div><span class="en">Basmati rice with fried berberis</span></div>
      <div class="dish"><div class="h"><span>Grilltomate<span class="veg">v</span></span><span>1,00</span></div><span class="en">Grilled tomato</span></div>
      <div class="dish"><div class="h"><span>Sir Torshi<span class="veg">v</span></span><span>4,00</span></div><div class="de">Eingelegter Knoblauch</div><span class="en">Pickled garlic</span></div>
      <div class="dish"><div class="h"><span>Brot<span class="veg">v</span></span><span>1,00</span></div><span class="en">Bread</span></div>
      <div class="dish"><div class="h"><span>Brot mit Sesam<span class="veg">v</span></span><span>1,50</span></div><span class="en">Bread with sesame</span></div>
    </div>
  </div>
  <h2 class="title" style="margin-top:12px">Desserts<span class="en">Desserts</span></h2>
  <div class="cols">
    <div>
      <div class="dish"><div class="h"><span>Bastani</span><span>7,50</span></div><div class="de">Safraneis mit Pistazien und Sahne Stückchen</div><span class="en">Saffron ice cream with pistachios and cream pieces</span></div>
      <div class="dish"><div class="h"><span>Makhlut</span><span>8,00</span></div><div class="de">Gemischtes Eis aus Bastani und Faludeh</div><span class="en">Mix ice cream from Bastani and Faludeh</span></div>
      <div class="dish"><div class="h"><span>Sholezard<span class="veg">v</span></span><span>5,00</span></div><div class="de">Safran-Reispudding mit Zimt, Pistazien und Mandeln</div><span class="en">Saffron rice pudding with cinnamon, pistachios and almonds</span></div>
      <div class="dish"><div class="h"><span>Schoko Lava-Kuchen mit Eis</span><span>10,00</span></div><span class="en">Chocolate lava cake with ice cream</span></div>
    </div>
    <div>
      <div class="dish"><div class="h"><span>Faludeh<span class="veg">v</span></span><span>6,00</span></div><div class="de">Persisches Glasnudel-Sorbet</div><span class="en">Persian glass noodle sorbet</span></div>
      <div class="dish"><div class="h"><span>Khorma ba Gerdu<span class="veg">v</span></span><span>6,00</span></div><div class="de">Datteln mit Walnüssen gefüllt</div><span class="en">Dates with walnut</span></div>
      <div class="dish"><div class="h"><span>Affogato</span><span>5,00</span></div><div class="de">Espresso mit einer Kugel Vanilleeis</div><span class="en">Espresso with a scoop of vanilla ice cream</span></div>
      <div class="dish"><div class="h"><span>Kuchen aus der Vitrine</span><span>5,00</span></div><span class="en">Cake from the showcase</span></div>
    </div>
  </div>
  <footer class="foot"><div class="legend"><span class="veg">v</span> Vegetarische Gerichte <span class="en">Vegetarian Dishes</span> &nbsp;&nbsp; <span class="veg">v</span> Vegane Gerichte <span class="en">Vegan Dishes</span></div>Haben Sie Fragen zu Zusatzstoffen und Allergenen? Bitte wenden Sie sich an unser Personal!<br><span class="en">Do you have questions about additives and allergens? Please ask our staff!</span><br>Alle Preise in Euro inklusive Mehrwertsteuer. <span class="en">All prices in Euro including VAT.</span></footer>
</section>

<section class="page p5">
  <div class="brand"><span class="dot"></span>NANEH</div>
  <div class="course">
    <h2 class="title" style="font-size:12.5px;margin:0 0 4px">3-Gang-Menü<span class="en">3-Course Menu</span></h2>
    <p style="font-size:8.5px">ab 2 Personen<br><span class="en">from 2 people</span></p>
    <h3 class="title">Vorspeise<span class="en">Starter</span></h3>
    <p>Gemischter Vorspeisenteller<br><span class="en">Mixed appetizer plate</span></p>
    <h3 class="title">Hauptgericht<span class="en">Main Dish</span></h3>
    <p>Gemischter Grillteller<br><span class="en">Mixed grill plate</span></p>
    <p>Gemischter Reisteller<br><span class="en">Mixed rice plate</span></p>
    <p>Schmorgericht<br><span class="en">Braised dish</span></p>
    <h3 class="title">Dessert<span class="en">Dessert</span></h3>
    <p>Dessert-Variation<br><span class="en">Dessert variation</span></p>
    <p style="margin-top:52px">45,00<br><span style="font-size:8.5px">pro Person</span><br><span class="en" style="font-size:8.5px">per person</span></p>
  </div>
  <footer class="foot">Haben Sie Fragen zu Zusatzstoffen und Allergenen? Bitte wenden Sie sich an unser Personal!<br><span class="en">Do you have questions about additives and allergens? Please ask our staff!</span><br>Alle Preise in Euro inklusive Mehrwertsteuer. <span class="en">All prices in Euro including VAT.</span></footer>
</section>

<section class="page p6">
  <div class="brand"><span class="dot"></span>NANEH</div>
  <h2 class="title">Digestive</h2>
  <div class="drinks blk">
    <div><div class="d"><span>Arak Nadim</span><span>2 cl</span><span>4,00</span></div><div class="d"><span>Amara Sicula</span><span>4 cl</span><span>5,00</span></div><div class="d"><span>Fernet</span><span>4 cl</span><span>5,00</span></div><div class="d"><span>Grappa</span><span>4 cl</span><span>6,00</span></div></div>
    <div><div class="d"><span>Waldherr</span><span>4 cl</span><span>5,00</span></div><div class="d"><span>Ouzo</span><span>4 cl</span><span>5,00</span></div><div class="d"><span>Rossolini</span><span>4 cl</span><span>5,00</span></div><div class="d"><span>Sambuca</span><span>2 cl</span><span>3,00</span></div></div>
  </div>
  <h2 class="title">Cognac</h2>
  <div class="drinks blk">
    <div><div class="d"><span>Harcourt V.S.O.P.</span><span>4 cl</span><span>8,00</span></div><div class="d"><span>Harcourt X.O.</span><span>4 cl</span><span>18,00</span></div></div>
    <div><div class="d"><span>Roland Marchet V.S.O.P.</span><span>4 cl</span><span>8,00</span></div><div class="d"><span>Roland Marchet X.O.</span><span>4 cl</span><span>18,00</span></div></div>
  </div>
  <h2 class="title">Whiskey Bourbon</h2>
  <div class="drinks blk">
    <div><div class="d"><span>Old Crane</span><span>4 cl</span><span>6,00</span></div></div>
    <div><div class="d"><span>Hollis Creek</span><span>4 cl</span><span>6,00</span></div></div>
  </div>
  <h2 class="title">Whiskey Irish and Canadian</h2>
  <div class="drinks blk">
    <div><div class="d"><span>Maple Ridge</span><span>4 cl</span><span>6,00</span></div><div class="d"><span>Tullagh Mist</span><span>4 cl</span><span>6,00</span></div></div>
    <div><div class="d"><span>Kilrowan</span><span>4 cl</span><span>6,50</span></div></div>
  </div>
  <h2 class="title">Whiskey Scotch</h2>
  <div class="drinks blk">
    <div><div class="d"><span>R&amp;T</span><span>4 cl</span><span>6,00</span></div><div class="d"><span>Highland Rover Red</span><span>4 cl</span><span>6,00</span></div></div>
    <div><div class="d"><span>Highland Rover Black</span><span>4 cl</span><span>6,00</span></div><div class="d"><span>Carran Royal</span><span>4 cl</span><span>7,00</span></div></div>
  </div>
  <h2 class="title">Whiskey Malt</h2>
  <div class="drinks blk">
    <div><div class="d"><span>Glenbrae</span><span>4 cl</span><span>7,00</span></div></div>
    <div><div class="d"><span>Glenfarrow</span><span>4 cl</span><span>7,00</span></div></div>
  </div>
  <h2 class="title">Vodka / Tequila</h2>
  <div class="drinks blk">
    <div><div class="d"><span>Nordvik</span><span>4 cl</span><span>5,00</span></div><div class="d"><span>Silver Heron</span><span>4 cl</span><span>9,00</span></div></div>
    <div><div class="d"><span>Solera Tequila</span><span>2 cl</span><span>3,50</span></div></div>
  </div>
  <footer class="foot">Haben Sie Fragen zu Zusatzstoffen und Allergenen? Bitte wenden Sie sich an unser Personal!<br><span class="en">Do you have questions about additives and allergens? Please ask our staff!</span><br>Alle Preise in Euro inklusive Mehrwertsteuer. <span class="en">All prices in Euro including VAT.</span></footer>
</section>

<section class="page p7">
  <div class="brand"><span class="dot"></span>NANEH</div>
  <h2 class="title">Softgetränke</h2>
  <div class="drinks blk" style="margin-bottom:10px">
    <div><div class="d2"><span>Wasser</span><span>0,2 l</span><span>2,90</span><span>0,75 l</span><span>7,50</span></div><div class="d2"><span>Kola Classic</span><span></span><span></span><span>0,33 l</span><span>3,50</span></div><div class="d2"><span>Cola Light</span><span></span><span></span><span>0,33 l</span><span>3,50</span></div><div class="d2"><span>Cola Zero</span><span></span><span></span><span>0,33 l</span><span>3,50</span></div><div class="d2"><span>Limonit</span><span></span><span></span><span>0,33 l</span><span>3,50</span></div><div class="d2"><span>Aranja</span><span></span><span></span><span>0,33 l</span><span>3,50</span></div></div>
    <div><div class="d"><span>Mischmasch</span><span>0,33 l</span><span>3,50</span></div><div class="d"><span>Bitter Lemon</span><span>0,2 l</span><span>3,50</span></div><div class="d"><span>Ginger Ale</span><span>0,2 l</span><span>3,50</span></div><div class="d"><span>Tonic Water</span><span>0,2 l</span><span>3,50</span></div><div class="d"><span>Wild Berry</span><span>0,2 l</span><span>3,50</span></div><div class="d"><span>Dough</span><span>0,25 l</span><span>3,50</span></div></div>
  </div>
  <h2 class="title">Säfte</h2>
  <div class="drinks blk" style="margin-bottom:10px">
    <div><div class="d"><span>Mangosaft</span><span>0,2 l</span><span>3,50</span></div><div class="d"><span>Rhabarbersaft</span><span>0,2 l</span><span>3,50</span></div><div class="d"><span>Johannisbeerensaft</span><span>0,2 l</span><span>3,50</span></div><div class="d"><span>Orangensaft</span><span>0,2 l</span><span>3,50</span></div><div class="d"><span>Ananassaft</span><span>0,2 l</span><span>3,50</span></div><div class="d"><span>Multivitamin</span><span>0,2 l</span><span>3,50</span></div><div class="d"><span>Kirschnektar</span><span>0,2 l</span><span>3,50</span></div></div>
    <div><div class="d"><span>Bananennektar</span><span>0,2 l</span><span>3,50</span></div><div class="d"><span>Maracujanektar</span><span>0,2 l</span><span>3,50</span></div><div class="d2"><span>Kiba</span><span>0,2 l</span><span>2,90</span><span>0,4 l</span><span>5,00</span></div><div class="d"><span>Tomatensaft</span><span>0,2 l</span><span>3,50</span></div><div class="d"><span>Apfelschorle Quellgold</span><span>0,3 l</span><span>3,50</span></div><div class="d2"><span>Saftschorle</span><span>0,2 l</span><span>3,50</span><span>0,4 l</span><span>5,00</span></div><div class="d"><span>Granatapfel Saft</span><span>0,25 l</span><span>4,50</span></div></div>
  </div>
  <h2 class="title">Warme Getränke</h2>
  <div class="drinks blk" style="margin-bottom:10px">
    <div><div class="d two"><span>Schwarzer Tee klein (aufgesetzt)</span><span>2,50</span></div><div class="d two"><span>Schwarzer Tee groß (aufgesetzt)</span><span>4,00</span></div><div class="d two"><span>Frischer Pfefferminztee</span><span>4,50</span></div><div class="d two"><span>Frischer Pfefferminztee mit Ingwer</span><span>5,00</span></div><div class="d two"><span>Loser Tee (nach Wahl)</span><span>5,00</span></div><div class="d two"><span>Espresso</span><span>2,50</span></div><div class="d two"><span>Doppelter Espresso</span><span>3,50</span></div><div class="d two"><span>Kaffee</span><span>2,90</span></div></div>
    <div><div class="d two"><span>Milchkaffee</span><span>3,80</span></div><div class="d two"><span>Cappuccino</span><span>3,80</span></div><div class="d two"><span>Latte Macchiato</span><span>3,80</span></div><div class="d two"><span>Espresso Macchiato</span><span>2,70</span></div><div class="d two" style="height:auto;line-height:1.2;padding-top:3px"><span>Milchhaltige Getränke<br>wahlweise mit (Aufpreis)<br>Laktosefreier Milch<br>Hafermilch</span><span><br><br>0,50<br>0,80</span></div></div>
  </div>
  <h2 class="title">Flaschenbiere (Lindhof)</h2>
  <div class="drinks blk" style="margin-bottom:10px">
    <div><div class="d"><span>Lindhof Pils</span><span>0,33 l</span><span>3,50</span></div><div class="d"><span>Lindhof alkoholfrei</span><span>0,33 l</span><span>3,50</span></div><div class="d"><span>Radler</span><span>0,33 l</span><span>3,50</span></div><div class="d"><span>Radler alkoholfrei</span><span>0,33 l</span><span>3,50</span></div></div>
    <div><div class="d"><span>Weizen hell / dunkel</span><span>0,5 l</span><span>5,00</span></div><div class="d"><span>Weizen alkoholfrei</span><span>0,5 l</span><span>5,00</span></div></div>
  </div>
  <h2 class="title">Longdrinks</h2>
  <div class="drinks">
    <div><div class="d two"><span>Vodka (Nordvik) Lemon</span><span>9,00</span></div><div class="d two"><span>Vodka (Nordvik) Volt</span><span>9,50</span></div><div class="d two"><span>Whiskey (Hollis Creek) Cola</span><span>9,50</span></div></div>
    <div><div class="d two"><span>Harbour Tonic</span><span>9,00</span></div><div class="d two"><span>Hartwell Tonic</span><span>10,50</span></div><div class="d two"><span>Cayo Blanco Cola</span><span>9,00</span></div></div>
  </div>
  <footer class="foot">Haben Sie Fragen zu Zusatzstoffen und Allergenen? Bitte wenden Sie sich an unser Personal!<br><span class="en">Do you have questions about additives and allergens? Please ask our staff!</span><br>Alle Preise in Euro inklusive Mehrwertsteuer. <span class="en">All prices in Euro including VAT.</span></footer>
</section>

<section class="page p8">
  <div class="brand big" style="height:168px"><span class="dot"></span>NANEH</div>
  <h2 class="title">Minz-Schorle</h2>
  <p class="note" style="font-size:8.5px;margin-bottom:6px">mit frischer Minze, Orange, Limette und Zitrone</p>
  <div class="drinks blk" style="margin-bottom:46px">
    <div><div class="d"><span>Rhabarber</span><span>0,4 l</span><span>5,00</span></div><div class="d"><span>Johannisbeere</span><span>0,4 l</span><span>5,00</span></div></div>
    <div><div class="d"><span>Maracuja</span><span>0,4 l</span><span>5,00</span></div><div class="d"><span>Mango</span><span>0,4 l</span><span>5,00</span></div></div>
  </div>
  <h2 class="title">Hausgemachte Limonade</h2>
  <div class="d" style="grid-template-columns:1fr 30px 36px;height:auto;align-items:start"><span>Safran-Zitronen-Limonade<br><span style="text-transform:none">mit Chia-Samen, Ingwer, Minze und Limette</span></span><span style="padding-top:5px">0,5 l</span><span style="padding-top:5px">5,50</span></div>
  <footer class="foot">Haben Sie Fragen zu Zusatzstoffen und Allergenen? Bitte wenden Sie sich an unser Personal!<br><span class="en">Do you have questions about additives and allergens? Please ask our staff!</span><br>Alle Preise in Euro inklusive Mehrwertsteuer. <span class="en">All prices in Euro including VAT.</span></footer>
</section>

</body>
</html>
```